Poetry Book Cover Design Project

Looking for a minimalistic book cover design for a collection of poems. The book title is "Before The Morning Turns To Glass". There are three parts to the book. First covers poetry in the theme of Rage. Second love and desire. The third is strange poems. Essentially the sections are "Rage", "Desire" and the "Strange". The reason for the title "Before The Morning Turns To Glass" is as if someone is writing these till life changes towards the intended outcome as felt in each poem. I want to have the author's name "Nirosha Kulathunge" at the bottom. Ilustration attached.
- Minimalistic

```html
<!DOCTYPE html>
<html lang="en">
<head>
<meta charset="UTF-8">
<title>Before The Morning Turns To Glass — Book Cover</title>
<link rel="stylesheet" href="https://fonts.googleapis.com/css2?family=Roboto+Slab:wght@400;700&display=swap">
<style>
  :root {
    --backdrop: #e6e6e6;
    --cover-cream: #f8ece2;
    --cover-cream-light: #fbf2ec;
    --cover-tan: #d6c9bb;
    --ink-blue: #0855a1;
    --sky-blue: #5aa8df;
  }
  * { margin: 0; padding: 0; box-sizing: border-box; }
  html, body {
    width: 1200px;
    height: 800px;
    overflow: hidden;
    background: var(--backdrop);
  }
  .canvas {
    position: relative;
    width: 1200px;
    height: 800px;
  }
  .book-cover {
    position: absolute;
    left: 400px;
    top: 40px;
    width: 400px;
    height: 720px;
    background: linear-gradient(to bottom,
      var(--cover-cream-light) 0%,
      var(--cover-cream) 20%,
      var(--cover-cream) 78%,
      var(--cover-tan) 100%);
    box-shadow: 0 10px 30px rgba(0, 0, 0, 0.12);
  }
  .cover-emblem {
    position: absolute;
    left: 52px;
    top: 190px;
    width: 110px;
    height: 330px;
    border-radius: 55px;
    background: linear-gradient(to bottom, var(--sky-blue), var(--ink-blue));
  }
  .book-title {
    position: absolute;
    right: 28px;
    top: 178px;
    font-family: "Roboto Slab", serif;
    font-weight: 700;
    font-size: 52px;
    line-height: 69px;
    letter-spacing: -1px;
    color: var(--ink-blue);
    text-align: right;
  }
  .book-title span { display: block; }
  .author-name {
    position: absolute;
    left: 0;
    right: 0;
    bottom: 44px;
    text-align: center;
    font-family: "Roboto Slab", serif;
    font-weight: 400;
    font-size: 14px;
    color: var(--ink-blue);
  }
</style>
</head>
<body>
<main class="canvas">
  <section class="book-cover">
    <div class="cover-emblem" role="img" aria-label="Stylised blue eye emblem"></div>
    <h1 class="book-title">
      <span>Before</span>
      <span>The</span>
      <span>Morning</span>
      <span>Turns</span>
      <span>To</span>
      <span>Glass</span>
    </h1>
    <p class="author-name">Nirosha Kulathunge</p>
  </section>
</main>
</body>
</html>
```